A5 Patient Information Booklet (Chiropractic Clinic) 4-8 pages

Here’s a polished, professional rewrite of your full brief and content, with clearer structure, corrected language, and a premium tone:

---

**Project Title:** Premium Patient Information Brochure (Chiropractic & Wellness Clinic)

---

### **Overview**

We are a health and wellness clinic seeking a premium, high-end patient information brochure to provide following a patient’s initial consultation and first treatment.

The purpose of this booklet is to:

* Reinforce trust and professionalism
* Help patients understand what to expect next
* Encourage adherence to care recommendations
* Position the clinic as calm, expert-led, and results-driven

---

### **Format**

* 4–8 page booklet (A5 or similar size)
* Print-ready and digital versions required

---

### **Target Audience**

Patients who have just completed their initial consultation and may have begun treatment. They may already be experiencing physical or mental changes, so the brochure should guide, reassure, and educate them on what comes next.

---

### **Tone & Style**

* Premium, calm, and reassuring
* Modern wellness aesthetic (not overly clinical)
* Clean layout with minimal clutter
* Soft, neutral colour palette (whites, creams, muted greens, soft blues)
* Elegant typography (e.g. Montserrat / Lato)
* High-end, trustworthy, and professional feel

---

### **Key Messages**

#### 1. Listen to Your Body

Patients may feel different after treatment. Reassure them that this is normal and part of the healing process.

#### 2. Post-Treatment Advice

* Stay well hydrated
* Rest if needed
* Avoid overexertion if the body requires recovery

#### 3. Healing is a Journey (Core Concept)

A strong visual metaphor of a **“road to recovery”** or **journey** should be central to the design.

This journey should clearly illustrate three phases:

* **Phase 1: Initial Care (Weeks 1–6)**
Focus: Reducing pain/discomfort, calming the body, and initiating response to treatment

* **Phase 2: Corrective Care (Weeks 6–12)**
Focus: Addressing underlying issues, improving function, and creating lasting change

* **Phase 3: Wellness / Maintenance (Ongoing)**
Focus: Maintaining progress, preventing relapse, and supporting long-term wellbeing

**Important:**

* Emphasise that this is not a quick fix
* Progress requires time and consistency
* Each patient follows an individualised care plan
* The journey should feel structured, positive, and achievable

#### 4. Personalised Care

Reinforce that every treatment plan is tailored specifically to the individual.

#### 5. Professional Reassurance

Patients should feel confident they are in expert hands and supported throughout their journey.

---

### **Design Direction**

* Use imagery that reflects calmness, progression, and wellness (e.g. pathways, nature, soft gradients)
* Avoid generic stock imagery
* **Only use original clinic images from website and social media**
* Prioritise white space and clarity
* Aim for a luxury spa/medical hybrid aesthetic

---

## **Content Structure (Page-by-Page)**

### **Front Cover**

* Clean, minimal, premium design
* Clinic branding

---

### **Page 1: Patient Case Summary**

**Title:** *Welcome to Fernwell Practice*

Thank you for choosing Fernwell Practice.

This booklet is designed to guide you through:

* What we found during your initial consultation
* Your personalised recommended treatment plan
* Your road to recovery
* Long-term wellness care
* Why we take the approach we do

---

### **Page 2: Your Care Journey**

**Stage 1: Your Initial Consultation**

Today we completed a comprehensive assessment of your health and function, including:

* Full case history and discussion of your symptoms and goals
* Orthopaedic and neurological testing
* Postural and movement assessment
* Initial treatment (where appropriate)

**What this tells us:**

* How your body is currently functioning
* Where areas of stress or dysfunction may be present
* The most appropriate and effective path forward for your care

---

### **Page 3: Your Suggested Treatment Plan**

Based on today’s findings, your recommended care plan is:

**______ treatments over ______ weeks**

This should be viewed alongside your *Road to Recovery* to help you understand what to expect.

We have also discussed:

* Expected timelines for improvement
* Available payment options

**After Treatment:**
It is common to feel different following treatment. This is a normal response as your body begins to adapt and respond.

We recommend:

* Staying well hydrated
* Allowing time for rest and recovery
* Avoiding overexertion if your body feels it needs it

---

### **Page 4: What to Expect Next**

Healing is not always linear—it is a process that occurs over time.

Your care will typically progress through the following stages:

* **Relief Care**
Focused on reducing discomfort and calming the body

* **Corrective Care**
Focused on addressing underlying issues and improving function
(This phase may include prescribed exercises)

* **Maintenance / Wellness Care**
Focused on sustaining progress, preventing recurrence, and supporting long-term health

---

### **Page 5: Understanding Chiropractic Care**

**What is Chiropractic?**
Chiropractic care focuses on the relationship between the spine, nervous system, and overall body function.

By improving spinal movement and alignment, chiropractic care helps support the nervous system, allowing the body to function and heal more effectively.

**About Fernwell Practice**
At Fernwell Practice, our approach is centred around personalised, patient-focused care. We aim to not only relieve symptoms but to address underlying causes and support long-term wellbeing.

---

### **Back Page**

* Clinic contact details
* Website
* Social media icons/handles

**Closing Message:**
“A healthier, stronger you—supported every step of the way.”

---

### **Deliverables**

* Print-ready PDF
* Editable source files

---

### **Additional Notes**

* The brochure should feel valuable and worth keeping
* Encourage long-term care in a subtle, non-pushy way
* Maintain clarity, readability, and strong visual hierarchy
* Balance professionalism with warmth and approachability

---

If you’d like, I can also turn this into **actual brochure copy (fully written, patient-facing text)** or help you refine it further for a designer.

Target Market(s)

Existing patients who want to feel better and look after themselves that is given after their initil consultation appointment

Industry/Entity Type

Chiropractic, wellness, health

Font styles to use
Other font styles liked:
• Montserrat or Lato

Colors
0094D4
00A9DD
6FCCEA
C7EBF8
E9F6FB
00AB8E
00BBA5
67D7C9
C6EFE9
E9F9F6
6B429C
8869AF
B7A5CE
E3DAEB
F3F0F8

Requirements
Must have
• my own photos, look premium wellness, be clear and simple to understand for patients journey or what to expect next and over time
Nice to have
• USe my social media/website for ideas
Should not have
• generic photos and images

```html
<!DOCTYPE html>
<html lang="en">
<head>
<meta charset="utf-8">
<title>Fernwell Practice – Patient Information Booklet</title>
<link rel="stylesheet" href="https://fonts.googleapis.com/css2?family=Montserrat:wght@300;400;500;600;700&family=Oswald:wght@500&family=Great+Vibes&display=swap">
<style>
:root{
  --board:#6e6e6e;
  --paper:#ffffff;
  --mist:#f3f8f8;
  --teal:#00ab8e;
  --teal-deep:#1f9e92;
  --teal-soft:#67d7c9;
  --teal-pale:#c6efe9;
  --teal-wash:#e9f6f4;
  --blue-soft:#c7ebf8;
  --purple:#6b429c;
  --purple-soft:#8869af;
  --purple-pale:#e3daeb;
  --ink:#222;
  --text:#3b3b3b;
  --line:#cfe6e2;
}
*{margin:0;padding:0;box-sizing:border-box}
html,body{width:1200px;height:1070px;overflow:hidden}
body{background:var(--board);font-family:'Montserrat',sans-serif;color:var(--text);position:relative}
.page{position:absolute;width:339px;height:480px;background:var(--paper);overflow:hidden}
.page > *{position:absolute}
.p-cover{left:55px;top:40px;background:var(--mist)}
.p-expect{left:431px;top:40px}
.p-journey{left:806px;top:40px;background:linear-gradient(180deg,#fafcfc,#f1f7f7)}
.p-plan{left:57px;top:549px;background:#fbfcfc}
.p-back{left:434px;top:551px}
.center{left:0;right:0;text-align:center}

/* brand */
.brand-mark{width:34px;height:34px;border-radius:50%;border:2px solid var(--teal-soft)}
.brand-name{font-weight:600;color:var(--ink);white-space:nowrap;letter-spacing:.02em}
.brand-tag{color:var(--teal);letter-spacing:.14em;font-weight:500;white-space:nowrap}

/* cover */
.cover-blob{left:-40px;top:-40px;width:200px;height:160px;border-radius:0 0 60% 40%;background:linear-gradient(140deg,#a9d8d1,#e6f3f1)}
.cover-road{left:0;top:340px;width:339px;height:140px;background:linear-gradient(160deg,#eef6f5 10%,#bfe3dd 55%,#9fd1c9)}
.cover-title{font-size:23px;font-weight:400;color:var(--ink);line-height:1}
.cover-script{font-family:'Great Vibes',cursive;font-size:38px;color:var(--teal-deep);line-height:1}
.divider{height:1px;background:var(--teal)}
.dot{width:4px;height:4px;border-radius:50%;background:var(--teal)}
.cover-lead{font-size:7.5px;color:var(--ink)}
.cover-lead span{display:block;color:var(--teal);margin-top:2px}
.cover-motto{font-size:5.8px;letter-spacing:.3em;color:var(--ink)}
.ring{width:18px;height:18px;border-radius:50%;border:1px solid var(--teal)}

/* expect */
.expect-title{font-family:'Oswald',sans-serif;font-size:22px;color:var(--ink);line-height:1}
.expect-sub{font-family:'Oswald',sans-serif;font-size:15px;color:var(--teal);line-height:1}
.body-s{font-size:6.6px;line-height:1.55;color:var(--text)}
.col-rule{width:1px;background:var(--line)}
.hr{height:1px;background:var(--line)}
.badge{width:24px;height:24px;border-radius:50%;background:var(--teal)}
.step-h{font-size:7.5px;font-weight:700;color:var(--ink);line-height:1.3}
.ticks{list-style:none;font-size:5.8px;line-height:1.7}
.ticks li::before{content:"";display:inline-block;width:4px;height:4px;border:1px solid var(--teal);border-radius:50%;margin-right:5px;vertical-align:middle}
.tip-h{font-size:6.4px;font-weight:600;color:var(--teal)}
.tip-p{font-size:5.8px;line-height:1.5;margin-top:2px}
.tip-icon{width:12px;height:16px;border:1px solid var(--teal);border-radius:2px}
.note-card{background:var(--teal-wash);border:1px solid var(--line);border-radius:6px}
.wave{background:linear-gradient(170deg,transparent 20%,#e2f3f0 55%,#f5fbfa)}
.callout-h{font-size:8.5px;font-weight:600;color:var(--teal)}
.callout-p{font-size:6.5px;color:var(--ink)}

/* journey */
.j-your{font-size:15px;letter-spacing:.06em;color:var(--ink);line-height:1}
.j-big{font-size:26px;font-weight:700;color:var(--teal);letter-spacing:.04em;line-height:1}
.j-road{background:linear-gradient(175deg,#cdeeea 0%,#7fd2c6 35%,#b7e1ec 65%,#c9b8df 100%);border-radius:40% 60% 0 30%/30% 50% 0 30%;opacity:.85}
.j-scale{background:#fff;border:1px solid #e4efee;border-radius:5px}
.scale-item{position:absolute;left:6px;display:flex;gap:4px;align-items:flex-start}
.scale-item i{width:10px;height:10px;border-radius:50%;background:var(--teal);flex:none}
.scale-item.low i{background:var(--purple-soft)}
.scale-item b{display:block;font-size:3.6px;color:var(--teal);font-weight:700}
.scale-item.low b{color:var(--purple)}
.scale-item span{font-size:3.4px;line-height:1.35;color:var(--text);display:block}
.phase-tag{font-size:4px;font-weight:700;color:#fff;background:var(--teal);padding:1px 3px;border-radius:1px}
.phase-h{font-size:6.3px;font-weight:600;color:var(--teal-deep);line-height:1.2}
.phase-w{font-size:3.8px;font-weight:600;color:var(--teal);letter-spacing:.05em}
.phase-f{font-size:3.6px;line-height:1.45;color:var(--text)}
.phase-f b{color:var(--ink)}
.pin{width:20px;height:20px;border-radius:50%;border:2px solid var(--teal);background:#fff}
.bubble{font-size:3.6px;color:var(--teal);background:#fff;border:1px solid var(--teal-pale);border-radius:6px;padding:2px 5px;line-height:1.3}
.strip{background:#fff;border:1px solid #e4efee;border-radius:4px;display:flex}
.strip div{flex:1;display:flex;gap:4px;padding:6px 5px;border-right:1px solid #e6eeee}
.strip div:last-child{border-right:0}
.strip i{width:13px;height:13px;border-radius:50%;border:1px solid var(--teal);flex:none}
.strip b{display:block;font-size:3.6px;color:var(--teal);font-weight:700}
.strip span{display:block;font-size:3.4px;line-height:1.35}
.j-foot{font-size:4.2px;color:var(--text)}
.j-foot b{display:block;color:var(--teal);font-size:4.4px;letter-spacing:.05em;margin-top:2px}

/* plan */
.plan-blob{left:-30px;top:-20px;width:190px;height:150px;border-radius:0 0 70% 30%;background:linear-gradient(150deg,#cdebe6,#f3f9f8)}
.plan-kicker{font-size:10px;letter-spacing:.28em;color:var(--teal);font-weight:500}
.plan-title{font-size:27px;font-weight:600;letter-spacing:.08em;color:var(--ink);line-height:1}
.field{left:32px;width:274px;border:1px solid #9fd6cd;border-radius:5px;background:#fff;overflow:hidden}
.field-side{position:absolute;left:0;top:0;bottom:0;width:37px;background:var(--teal-deep)}
.field-label{position:absolute;font-size:5.6px;font-weight:600;color:var(--teal-deep);letter-spacing:.03em}
.rule{position:absolute;left:82px;right:16px;height:1px;background:#cfe3e0}
.rule.strong{background:var(--teal)}
.slot{position:absolute;width:52px;height:13px;border:1px solid #9fd6cd;border-radius:2px}
.plan-script{font-family:'Great Vibes',cursive;font-size:12px;color:var(--teal-deep)}

.back-word{font-size:32px;font-weight:700;color:#6cc8b6;letter-spacing:.04em}
</style>
</head>
<body>

<!-- Front cover -->
<section class="page p-cover">
  <div class="cover-blob"></div>
  <div class="cover-road" role="img" aria-label="Soft teal winding road fading into the distance"></div>
  <div class="brand-mark" style="left:152px;top:62px"></div>
  <div class="brand-name center" style="top:124px;font-size:12px">FERNWELL PRACTICE</div>
  <div class="brand-tag center" style="top:141px;font-size:5.8px">CHIROPRACTIC &amp; WELLNESS</div>
  <div class="cover-title center" style="top:171px">Your Healing</div>
  <div class="cover-script center" style="top:195px">Journey</div>
  <div class="cover-title center" style="top:236px">Starts Here</div>
  <div class="divider" style="left:142px;top:271px;width:22px"></div>
  <div class="dot" style="left:167px;top:269px"></div>
  <div class="divider" style="left:175px;top:271px;width:22px"></div>
  <div class="cover-lead center" style="top:287px">Personalised care. Lasting results.<span>A healthier you, every step of the way.</span></div>
  <div class="ring" style="left:160px;top:413px"></div>
  <div class="cover-motto center" style="top:441px">RESTORE • REBALANCE • THRIVE</div>
</section>

<!-- What to expect -->
<section class="page p-expect">
  <div class="brand-mark" style="left:66px;top:18px"></div>
  <div class="brand-name" style="left:20px;top:60px;width:130px;text-align:center;font-size:7.8px">FERNWELL PRACTICE</div>
  <div class="brand-tag" style="left:20px;top:71px;width:130px;text-align:center;font-size:3.6px">CHIROPRACTIC &amp; WELLNESS</div>
  <div class="expect-title" style="left:21px;top:97px">WHAT TO EXPECT</div>
  <div class="expect-sub" style="left:21px;top:121px">AFTER YOUR TREATMENT</div>
  <div class="divider" style="left:21px;top:147px;width:28px;height:1.5px"></div>
  <p class="body-s" style="left:21px;top:157px;width:132px">It's normal to experience some changes as your body responds and begins to heal. Here's what you may notice and how you can support your recovery.</p>
  <div class="wave" style="left:0;top:225px;width:168px;height:120px" role="img" aria-label="Soft teal wave with a leafy sprig"></div>
  <div class="note-card" style="left:18px;top:307px;width:131px;height:60px"></div>
  <div class="ring" style="left:25px;top:325px;width:20px;height:20px"></div>
  <p class="tip-p" style="left:54px;top:314px;width:90px;font-size:5.6px"><b style="color:var(--teal)">Every body is unique.</b><br>Your response to treatment is normal and part of your healing journey. We're here to support you every step of the way.</p>

  <div class="col-rule" style="left:169px;top:33px;height:342px"></div>

  <div class="badge" style="left:185px;top:39px"></div>
  <div class="step-h" style="left:216px;top:42px">1. YOUR BODY<br>IS RESPONDING</div>
  <p class="tip-p" style="left:186px;top:70px;width:118px">After treatment, your body may begin to release tension and restore balance. You might feel different in ways such as:</p>
  <ul class="ticks" style="left:186px;top:98px">
    <li>Improved mobility</li><li>Mild soreness</li><li>Tiredness or relaxation</li><li>Emotional shifts</li>
  </ul>
  <div class="hr" style="left:186px;top:147px;width:126px"></div>

  <div class="badge" style="left:185px;top:158px"></div>
  <div class="step-h" style="left:216px;top:161px">2. SUPPORT YOUR<br>RECOVERY</div>
  <div class="tip-icon" style="left:189px;top:194px"></div>
  <div class="tip-h" style="left:216px;top:190px">Stay Hydrated</div>
  <p class="tip-p" style="left:216px;top:198px;width:96px">Drink plenty of water to help flush toxins and support healing.</p>
  <div class="hr" style="left:186px;top:223px;width:126px"></div>
  <div class="tip-icon" style="left:187px;top:236px;width:18px;height:10px"></div>
  <div class="tip-h" style="left:216px;top:231px">Rest if Needed</div>
  <p class="tip-p" style="left:216px;top:239px;width:96px">Allow your body the time and rest it needs to repair and rebalance.</p>
  <div class="hr" style="left:186px;top:264px;width:126px"></div>
  <div class="tip-icon" style="left:191px;top:275px;width:8px;height:20px;border-radius:4px"></div>
  <div class="tip-h" style="left:216px;top:272px">Avoid Overexertion</div>
  <p class="tip-p" style="left:216px;top:280px;width:96px">Postpone intense activities if your body feels it needs recovery time.</p>
  <div class="hr" style="left:186px;top:308px;width:126px"></div>

  <div class="badge" style="left:185px;top:318px"></div>
  <div class="step-h" style="left:216px;top:321px">3. LISTEN TO<br>YOUR BODY</div>
  <p class="tip-p" style="left:186px;top:347px;width:110px">Pay attention to how you feel.<br>It's okay to take it slow and give your body what it needs.</p>

  <div class="hr" style="left:28px;top:396px;width:36px;background:var(--teal-pale)"></div>
  <div class="ring" style="left:76px;top:385px;width:24px;height:24px"></div>
  <div class="callout-h" style="left:107px;top:387px">Healing is a process, not a quick fix.</div>
  <div class="callout-p" style="left:107px;top:399px">Consistency and care create lasting change.</div>
  <div class="hr" style="left:270px;top:396px;width:40px;background:var(--teal-pale)"></div>
  <div class="note-card" style="left:29px;top:418px;width:281px;height:41px;border:0"></div>
  <div class="ring" style="left:46px;top:426px;width:25px;height:25px"></div>
  <p class="tip-p" style="left:82px;top:428px;width:150px;color:var(--ink)">We are here to guide and support you on your journey to better health and wellbeing.<br><b style="color:var(--teal)">Your best health starts with informed care.</b></p>
</section>

<!-- Recovery journey -->
<section class="page p-journey">
  <div class="j-your" style="left:24px;top:22px">YOUR</div>
  <div class="j-big" style="left:24px;top:37px">RECOVERY</div>
  <div class="j-your" style="left:24px;top:62px;font-size:22px">JOURNEY</div>
  <div class="divider" style="left:24px;top:88px;width:22px"></div>
  <div class="brand-mark" style="left:250px;top:22px;width:32px;height:32px"></div>
  <div class="brand-name" style="left:220px;top:61px;width:92px;text-align:center;font-size:6.4px">FERNWELL PRACTICE</div>
  <div class="brand-tag" style="left:220px;top:70px;width:92px;text-align:center;font-size:3.2px">CHIROPRACTIC &amp; WELLNESS</div>
  <div style="left:24px;top:97px;font-size:6px;font-weight:500;color:var(--teal);letter-spacing:.04em">HEALING IS A JOURNEY, NOT A QUICK FIX.</div>
  <p class="tip-p" style="left:24px;top:107px;width:130px;font-size:5.2px">True and lasting results take time, consistency and a personalised approach.<br>We're here to guide and support you every step of the way.</p>

  <div class="j-road" style="left:40px;top:135px;width:235px;height:290px" role="img" aria-label="Winding road climbing from purple to teal with three phase pins"></div>

  <div class="j-scale" style="left:25px;top:148px;width:70px;height:235px"></div>
  <div class="scale-item" style="top:155px;left:31px"><i></i><div><b>OPTIMISING</b><span>Peak performance<br>&amp; long-term wellbeing</span></div></div>
  <div class="scale-item" style="top:183px;left:31px"><i></i><div><b>ENHANCING</b><span>Improved function<br>&amp; greater movement</span></div></div>
  <div class="scale-item" style="top:211px;left:31px"><i></i><div><b>CORRECTING</b><span>Addressing the<br>root cause</span></div></div>
  <div class="scale-item" style="top:236px;left:31px"><i></i><div><b>STABILISING</b><span>Restoring balance<br>&amp; reducing compensation</span></div></div>
  <div class="scale-item" style="top:264px;left:31px"><i></i><div><b>STRENGTHENING</b><span>Building strength<br>&amp; resilience</span></div></div>
  <div class="scale-item" style="top:288px;left:31px"><i></i><div><b>HEALING</b><span>Supporting your<br>body to heal</span></div></div>
  <div class="scale-item low" style="top:313px;left:31px"><i></i><div><b>RECOVERING</b><span>Noticeable<br>improvements</span></div></div>
  <div class="scale-item low" style="top:337px;left:31px"><i></i><div><b>IMPROVING</b><span>Better everyday<br>function</span></div></div>
  <div class="scale-item low" style="top:362px;left:31px"><i></i><div><b>SUFFERING</b><span>Pain &amp; frustration<br>take over</span></div></div>

  <div class="pin" style="left:226px;top:138px"></div>
  <div class="bubble" style="left:255px;top:152px">Being your best,<br>every day</div>
  <div class="phase-tag" style="left:258px;top:179px">PHASE 3</div>
  <div class="phase-h" style="left:258px;top:188px">WELLNESS<br>MAINTENANCE</div>
  <div class="phase-w" style="left:258px;top:205px">ONGOING</div>
  <p class="phase-f" style="left:258px;top:212px;width:60px"><b>Focus:</b> Maintaining progress, preventing relapse, and supporting long-term health and wellbeing.</p>

  <div class="pin" style="left:184px;top:225px"></div>
  <div class="phase-tag" style="left:233px;top:258px">PHASE 2</div>
  <div class="phase-h" style="left:233px;top:268px">CORRECTIVE CARE</div>
  <div class="phase-w" style="left:233px;top:277px">WEEKS 6 – 12</div>
  <p class="phase-f" style="left:233px;top:284px;width:62px"><b>Focus:</b> Addressing underlying issues, improving function, and creating more stable, lasting changes.</p>

  <div class="pin" style="left:121px;top:278px;width:24px;height:24px"></div>
  <div class="phase-tag" style="left:137px;top:312px">PHASE 1</div>
  <div class="phase-h" style="left:137px;top:321px">INITIAL CARE</div>
  <div class="phase-w" style="left:137px;top:330px">WEEKS 1 – 6</div>
  <p class="phase-f" style="left:137px;top:337px;width:62px"><b>Focus:</b> Reducing pain and discomfort, calming the body, and helping you begin to respond to care.</p>

  <div class="bubble" style="left:92px;top:387px;color:var(--purple-soft)">Starting your<br>healing journey</div>

  <div class="note-card" style="left:236px;top:318px;width:75px;height:70px;background:#f7fbfb"></div>
  <div class="ring" style="left:244px;top:324px;width:14px;height:14px"></div>
  <div style="left:261px;top:326px;font-size:4.2px;font-weight:700;color:var(--teal-deep);line-height:1.3">PERSONALISED<br>FOR YOU</div>
  <p class="phase-f" style="left:244px;top:348px;width:62px">Your care plan is tailored specifically to you, your body, and your goals.<br><b>We're with you for the long run.</b></p>

  <div class="strip" style="left:25px;top:410px;width:285px;height:34px">
    <div><i></i><p><b>INDIVIDUAL CARE</b><span>Your plan is designed around you.</span></p></div>
    <div><i></i><p><b>EVIDENCE BASED</b><span>We use proven methods you can trust.</span></p></div>
    <div><i></i><p><b>LONG-TERM RESULTS</b><span>Sustainable change takes time.</span></p></div>
    <div><i></i><p><b>BETTER EVERYDAY</b><span>More energy, less pain, better life.</span></p></div>
  </div>
  <div class="hr" style="left:29px;top:456px;width:278px;background:var(--teal-soft)"></div>
  <div class="j-foot center" style="top:459px">Consistency today leads to a stronger, healthier tomorrow.<b>TOGETHER, WE'LL HELP YOU THRIVE.</b></div>
</section>

<!-- Care plan -->
<section class="page p-plan">
  <div class="plan-blob"></div>
  <div class="brand-mark" style="left:153px;top:18px;width:36px;height:36px"></div>
  <div class="brand-name center" style="top:59px;font-size:7.8px">FERNWELL PRACTICE</div>
  <div class="brand-tag center" style="top:69px;font-size:3.6px">CHIROPRACTIC &amp; WELLNESS</div>
  <div class="plan-kicker center" style="top:87px">YOUR PERSONALISED</div>
  <div class="plan-title center" style="top:100px">CARE PLAN</div>
  <div class="divider" style="left:143px;top:133px;width:22px"></div>
  <div class="dot" style="left:168px;top:131px"></div>
  <div class="divider" style="left:176px;top:133px;width:22px"></div>
  <p class="body-s center" style="top:140px;font-size:6.2px;color:var(--ink)">Every body is unique. Your care plan is specifically<br>designed to support your individual journey to better health.</p>

  <div class="field" style="top:173px;height:42px">
    <div class="field-side"></div>
    <div class="field-label" style="left:49px;top:11px">PATIENT NAME</div>
    <div class="rule strong" style="left:49px;top:29px"></div>
  </div>
  <div class="field" style="top:222px;height:88px">
    <div class="field-side"></div>
    <div class="field-label" style="left:49px;top:9px">SUGGESTED CARE PLAN</div>
    <div class="rule" style="left:49px;top:27px"></div>
    <div class="rule" style="left:49px;top:41px"></div>
    <div class="rule" style="left:49px;top:55px"></div>
    <div class="rule" style="left:49px;top:69px"></div>
    <div class="rule" style="left:49px;top:82px"></div>
  </div>
  <div class="field" style="top:319px;height:46px">
    <div class="field-side"></div>
    <div class="field-label" style="left:50px;top:10px">NUMBER OF TREATMENTS</div>
    <div class="slot" style="left:50px;top:22px"></div>
    <div style="position:absolute;left:154px;top:7px;width:1px;height:30px;background:#cfe3e0"></div>
    <div class="field-label" style="left:168px;top:10px">WEEKS DURATION</div>
    <div class="slot" style="left:168px;top:22px"></div>
  </div>
  <div class="note-card" style="left:32px;top:375px;width:274px;height:45px"></div>
  <div class="badge" style="left:48px;top:384px;width:28px;height:28px;background:var(--teal-deep)"></div>
  <div style="left:92px;top:385px;font-size:5.6px;font-weight:600;color:var(--teal-deep)">WE'RE WITH YOU EVERY STEP OF THE WAY.</div>
  <p class="tip-p" style="left:92px;top:394px;width:200px;font-size:4.6px">Our goal is to help you feel better, move better, and live better.<br>Consistency and commitment to your plan are key to long-term results.</p>
  <div class="plan-script center" style="top:432px">Together, we can achieve your best health.</div>
  <div class="hr" style="left:32px;top:456px;width:274px;background:var(--teal-soft)"></div>
</section>

<!-- Back page -->
<section class="page p-back">
  <div class="back-word center" style="top:220px">BACK PAGE</div>
</section>

</body>
</html>
```